Wordpress Design Papa Academy Project

Need a homepage design for a wordpress site that is based around becoming a better Dad. The sitemap file and logo file are attached. Navigation should be a combination of horizontal and vertical because the sitemap is extensive. I think the Father's conference, Daddy daughter dance and Essay contest would like nice if they were highlighted in their own rounded boxes at the bottom of the home page perhaps. New design needs to be attention grabbing, colorful but not over the top or too flashy either. I would like the background to be pictures and/or transparent words(similar to this site http://kinhearth.com/). Need a banner image which will be a slider and I need text overlay at the bottom of each image. I like rounded boxes like how this site showcases the news and events sections - http://www.qz.edu/. Need to also incorporate an events calendar, facebook and twitter icons and contact info. A preliminary design was initially created and is attached for you to review. Design needs to be balanced as there is alot of info to display.I have a current site here http://www.papaacad.com/ and you will see why I need a new design.
Updates

Reason: Still seeking creative concepts.

Reason: Still finalizing the design.

Target Market(s)

Dads

Industry/Entity Type

Events

Requirements
Must have
• image slider with text overlay on image, combination of horizontal and vertical navigation, show a dropdown menu under one of the horizontal tabs, events calendar, web safe fonts, colorful, use stock images for any placeholders,footer with sitemap
Nice to have
• rounded boxes, highlight father's conference,daddy daughter dance and essay contest in a separate section from the navigation, also put campus book store and online classes in a vertical nav bar perhaps - maybe in bigger placeholders like stacked boxes or similar.

```html
<!DOCTYPE html>
<html lang="en">
<head>
<meta charset="utf-8">
<title>Papa Academy – Home</title>
<link rel="stylesheet" href="https://fonts.googleapis.com/css2?family=Arimo:wght@400;700&family=Open+Sans:wght@400;600&display=swap">
<style>
:root{
  --navy:#1d3a4f;
  --navy-dark:#142b3b;
  --blue-link:#2a8bc4;
  --title-blue:#1f5f8f;
  --text:#555c62;
  --heading:#2b3338;
  --line:#d5d9dc;
  --panel:#ffffff;
  --page:#f2f4f6;
  --header-top:#eef2f8;
  --green:#5aa81e;
  --green-dark:#3f8a12;
  --footer:#eceeef;
  --footer-bar:#dfe1e3;
  --red:#d2313a;
}
*{box-sizing:border-box;margin:0;padding:0}
html,body{width:779px;height:1200px;overflow:hidden}
body{position:relative;background:var(--page);font-family:Arimo,Arial,sans-serif;color:var(--text)}
a{text-decoration:none;color:inherit}

.site-header{position:absolute;left:0;top:0;width:779px;height:86px;background:linear-gradient(#f8fafd,var(--header-top));display:flex;align-items:center;justify-content:center;gap:12px}
.brand-mark{width:38px;height:38px;background:var(--title-blue);border-radius:4px}
.brand-name{font-family:"Open Sans",Arial,sans-serif;font-size:22px;font-weight:600;color:var(--navy)}

.main-nav{position:absolute;left:0;top:86px;width:779px;height:31px;background:linear-gradient(#24465e,var(--navy));border-bottom:1px solid #0e2230}
.main-nav ul{list-style:none;display:flex;justify-content:center;height:100%;padding-right:10px}
.main-nav li{font-family:"Open Sans",Arial,sans-serif;font-size:10.5px;color:#e8eef3;display:flex;align-items:center;padding:0 14px}
.main-nav li.active{background:var(--navy-dark)}

.hero{position:absolute;left:0;top:117px;width:779px;height:460px;background:
  linear-gradient(to bottom,rgba(242,244,246,0) 70%,var(--page) 100%),
  linear-gradient(100deg,#9fb3c6 0%,#b9c4cc 35%,#7c6a55 60%,#a38a62 80%,#c6b08a 100%)}
.hero-title{position:absolute;left:120px;top:106px;font-family:"Open Sans",Arial,sans-serif;font-size:18.5px;line-height:24px;color:#1e2b33}
.hero-btn{position:absolute;left:120px;top:182px;width:120px;height:29px;background:linear-gradient(#ffffff,#dcdfe1);border:1px solid #bfc4c7;border-radius:2px;font-family:"Open Sans",Arial,sans-serif;font-size:12px;color:#333;display:flex;align-items:center;justify-content:center}

.content-panel{position:absolute;left:80px;top:418px;width:619px;height:560px;background:var(--panel);box-shadow:0 0 6px rgba(0,0,0,.12)}
.promo-strip{height:56px;border-bottom:1px solid var(--line);display:flex;align-items:center;justify-content:space-between;padding:0 11px 0 13px}
.promo-strip p{font-family:"Open Sans",Arial,sans-serif;font-size:10.5px;color:#333}
.btn-green{width:132px;height:32px;background:linear-gradient(#6dbe2c,var(--green-dark));border-radius:2px;color:#fff;font-family:"Open Sans",Arial,sans-serif;font-size:11px;display:flex;align-items:center;justify-content:center}

.welcome{padding:12px 16px 0}
.welcome h1{font-family:"Open Sans",Arial,sans-serif;font-weight:400;font-size:15.5px;color:var(--heading);display:flex;align-items:center;gap:14px;margin-left:-4px}
.welcome h1 .mark{width:20px;height:20px;background:var(--title-blue);border-radius:2px}
.welcome p{font-size:8.6px;line-height:13.4px;margin-top:13px}
.welcome p:first-of-type{margin-top:14px}

.feature-boxes{position:absolute;left:88px;top:735px;display:flex;gap:9px}
.feature{width:144px;height:219px;background:#fff;border:1px solid #b8bfc4;border-radius:4px;overflow:hidden;box-shadow:0 1px 3px rgba(0,0,0,.15)}
.feature h2{height:30px;background:linear-gradient(#2c5672,var(--navy));color:#fff;font-family:"Open Sans",Arial,sans-serif;font-weight:400;font-size:11.5px;display:flex;align-items:center;padding-left:13px}
.feature ul{list-style:none;padding:6px 13px 0}
.feature li{font-size:8.3px;line-height:16.3px;border-bottom:1px dotted #aeb4b8;color:#50575c}
.product-img{width:86px;height:90px;margin:13px auto 0;background:linear-gradient(#e4d8c0,#cbb995);border-radius:3px}
.product-name{text-align:center;color:var(--blue-link);font-size:11.5px;margin-top:14px}
.slider-arrows{display:flex;justify-content:space-between;padding:0 18px;margin-top:12px}
.slider-arrows span{width:14px;height:14px;border-radius:50%;border:1px solid #9aa0a4;background:#f4f4f4;display:flex;align-items:center;justify-content:center}
.essay-img{width:106px;height:74px;margin:15px auto 0;border:3px solid #fff;outline:1px solid #c6cbce;background:linear-gradient(#9fc4da,#5f8da8)}
.essay-caption{text-align:center;font-size:8.5px;margin-top:18px}
.btn-blue{display:flex;margin:10px auto 0;width:104px;height:18px;background:linear-gradient(#3aa0de,#1d79b5);color:#fff;font-size:8.5px;align-items:center;justify-content:center;border-radius:2px}

.site-footer{position:absolute;left:0;top:980px;width:779px;height:170px;background:var(--footer);border-top:1px solid #dcdfe2}
.footer-col{position:absolute;top:20px}
.footer-col h3{font-family:"Open Sans",Arial,sans-serif;font-weight:400;font-size:10px;color:var(--blue-link);letter-spacing:.2px}
.quick-links{left:95px}
.quick-links ul{list-style:none;margin-top:15px;width:120px}
.quick-links li{font-size:8.5px;line-height:16.5px;border-bottom:1px solid #c9cdd0;color:#4e5458}
.blog{left:255px}
.blog .post{width:115px;margin-top:16px;font-size:7.6px;line-height:11px;color:#4e5458;padding-left:3px}
.blog .post + .post{border-top:1px solid #c9cdd0;padding-top:8px;margin-top:8px}
.blog .meta{margin-top:1px}
.blog .meta span{color:var(--blue-link)}
.calendar{left:410px}
.cal{margin-top:15px;width:124px;background:#fff;border-radius:3px;overflow:hidden;box-shadow:0 1px 2px rgba(0,0,0,.15)}
.cal-head{height:13px;background:linear-gradient(#3b8cc9,#1f6aa5);color:#fff;font-size:7.5px;font-weight:700;display:flex;align-items:center;justify-content:center}
.cal table{border-collapse:collapse;width:100%;font-size:6.3px;color:#333}
.cal th{font-weight:700;background:#e8eaec;height:10px}
.cal td{text-align:center;height:10.7px}
.cal td.wk{color:#999;background:#f1f2f3}
.cal td.today{color:var(--red);font-weight:700}
.contact{left:564px}
.contact address{font-style:normal;font-size:8.3px;line-height:13.2px;color:#4e5458;margin-top:16px}
.contact .phone{margin-top:14px}

.footer-bar{position:absolute;left:0;top:1150px;width:779px;height:50px;background:var(--footer-bar);display:flex;align-items:center;justify-content:space-between;padding:0 84px 0 95px;font-size:8.3px;color:#333}
.footer-bar nav{display:flex;gap:16px}
</style>
</head>
<body>

<header class="site-header">
  <span class="brand-mark"></span>
  <span class="brand-name">Papa Academy, Inc.</span>
</header>

<nav class="main-nav">
  <ul>
    <li class="active">Home</li>
    <li>About us</li>
    <li>Admissions</li>
    <li>Information</li>
    <li>Services</li>
    <li>Blog</li>
    <li>Contact Us</li>
  </ul>
</nav>

<section class="hero" role="img" aria-label="Photo of a father reading a newspaper outdoors in tall grass with his son on his shoulders">
  <h2 class="hero-title">We Provide dads with the<br>tools to succeed.</h2>
  <a class="hero-btn">READ MORE</a>
</section>

<main class="content-panel">
  <div class="promo-strip">
    <p>Duis aute irure dolor in reprehenderit in voluptate velit esse cillum dolore eu fugiat nulla.</p>
    <a class="btn-green">View Online Classes</a>
  </div>
  <article class="welcome">
    <h1><span class="mark"></span>Welcome to Papa Academy</h1>
    <p>Papa Academy is dedicated to helping all fathers appreciate themselves and the responsibility of fatherhood. We cater to soon to be fathers, new fathers, existing fathers, and second time parents. As Fathers we find ourselves in a strange situation, sometimes not knowing what is right, what is best, or what to say. But we are always, always looked to as leaders. In this situation, we must band together to help one another with the greatest responsibility of all, the rise or demise of the next generation.</p>
    <p>Our goal is simply, to heal the world one father and child at a time. Our plan is to use all available resources to create a one-stop site for fatherhood. By helping them understand the importance their role has on the future of children throughout the world. We can bring them closer to their families through educating them on pregnancy, maternity, child bearing, and quality time which will help produce a strong minded, loved, and whole child. Where leaders come to learn!</p>
    <p>Papa Academy will help fathers deal with any obstacle. With our information and product line, we will aid them in understanding a father's role and how important it is to the world. May it be child rearing, family involvement, problems with mother, or just plain want to vent. We will be here. We have bonded together to help one another realize the dream of fatherhood. Being a father means, walking in the park hand in hand, teaching a child how to fish, watching their eyes light up when a train goes by. These are the things that make us, that complete us. But the road is uneven, and sometimes unfair, we will be that safe passage.</p>
  </article>
</main>

<section class="feature-boxes">
  <div class="feature">
    <h2>Our Products</h2>
    <div class="product-img" role="img" aria-label="Photo of a canvas tote bag"></div>
    <p class="product-name">Bags for Dad</p>
    <div class="slider-arrows">
      <span><svg width="6" height="6" viewBox="0 0 6 6"><path d="M4 0.5 L1.5 3 L4 5.5" fill="none" stroke="#555" stroke-width="1.2"/></svg></span>
      <span><svg width="6" height="6" viewBox="0 0 6 6"><path d="M2 0.5 L4.5 3 L2 5.5" fill="none" stroke="#555" stroke-width="1.2"/></svg></span>
    </div>
  </div>
  <div class="feature">
    <h2>Fathers Conference</h2>
    <ul>
      <li>Advisory Board</li><li>Event Agenda</li><li>Picture gallery</li><li>Request for Proposals</li><li>Vendor Opportunities</li><li>Sponsorship Opportunities</li><li>Conference Registration</li><li>Conference Resources</li><li>Testimony</li><li>Outcome reports</li>
    </ul>
  </div>
  <div class="feature">
    <h2>Dad Essay Contest</h2>
    <div class="essay-img" role="img" aria-label="Photo of a father and child silhouetted by the sea"></div>
    <p class="essay-caption">Picture gallery</p>
    <a class="btn-blue">Essay Submission</a>
  </div>
  <div class="feature">
    <h2>Daddy Daughter Dance</h2>
    <ul>
      <li>Event Agenda</li><li>Picture gallery</li><li>Vendor Opportunities</li><li>Sponsorship Opportunities</li><li>DDR Resources</li><li>Dance Registration</li><li>Testimony</li><li>Outcome reports</li>
    </ul>
  </div>
</section>

<footer class="site-footer">
  <div class="footer-col quick-links">
    <h3>QUICK LINKS</h3>
    <ul>
      <li>About Us</li><li>Information</li><li>Admissions</li><li>Products</li><li>Fathers Conference</li><li>Daddy Daughter Dance</li><li>Dad Eassy Contest</li>
    </ul>
  </div>
  <div class="footer-col blog">
    <h3>LATEST BLOG POST</h3>
    <div class="post">Lorem ipsum dolor sit amet, consectetur adipisicing elit, sed do eiusmod tempor incididunt.<p class="meta"><span>ut labore</span> @ 28.11.2012</p></div>
    <div class="post">Lorem ipsum dolor sit amet, consectetur adipisicing elit, sed do eiusmod tempor incididunt.<p class="meta"><span>ut labore</span> @ 28.11.2012</p></div>
  </div>
  <div class="footer-col calendar">
    <h3>EVENTS CALENDAR</h3>
    <div class="cal">
      <div class="cal-head">December 2012</div>
      <table>
        <tr><th>Wk</th><th>Su</th><th>Mo</th><th>Tu</th><th>We</th><th>Th</th><th>Fr</th><th>Sa</th></tr>
        <tr><td class="wk">48</td><td></td><td></td><td></td><td></td><td></td><td></td><td>1</td></tr>
        <tr><td class="wk">49</td><td>2</td><td>3</td><td>4</td><td>5</td><td>6</td><td>7</td><td>8</td></tr>
        <tr><td class="wk">50</td><td>9</td><td>10</td><td>11</td><td>12</td><td>13</td><td>14</td><td>15</td></tr>
        <tr><td class="wk">51</td><td>16</td><td>17</td><td>18</td><td>19</td><td>20</td><td>21</td><td>22</td></tr>
        <tr><td class="wk">52</td><td>23</td><td>24</td><td class="today">25</td><td>26</td><td>27</td><td>28</td><td>29</td></tr>
        <tr><td class="wk">1</td><td>30</td><td>31</td><td></td><td></td><td></td><td></td><td></td></tr>
      </table>
    </div>
  </div>
  <div class="footer-col contact">
    <h3>CONTACT</h3>
    <address>12345 Street Name<br>City Name,<br>State, Province, 12345 Zip Code<br>Country<p class="phone">Phone: (123) 456-789</p></address>
  </div>
</footer>

<div class="footer-bar">
  <p>Copyright © 2012 Papa Academy. All Rights Reserved.</p>
  <nav><a>Home</a><a>Blog</a><a>FAQ</a><a>Contact</a></nav>
</div>

</body>
</html>
```